high end kitchens , needing new logo and business card design .

im looking a very simple looking design but classy that will stand out , i would like the design to be in the colours black , silver , gold and grey , although all colours dont need to be used in design , back of card to have name on it colin farrow , address and phone number and website address , maybe fb logo . adrress is 27 orchard row , newtownards , bt19 4qd , 07812459067 , front of the card im open to design , back of card very simple i will want it matt black with silver writing , writing doesnt need to be that big

Target Market(s)

people with kitchen projects .

Industry/Entity Type

Interior Design

Contact Information for Business Card

front of business card lg on it with maybe lumen galley under it wrote smaller , maybe the card to be mate black with the writing in a gloss black or silver

Logo Text

lg . lumen galley

Font styles to use
Sans Serif
Script

Colors
1b1b1b
919191
f6f6f6
848484
ffc214
ec1f27

Requirements
Must have
• clean and simple , not too fussy ,
Nice to have
• n/a
Should not have
• n/a

```html
<!DOCTYPE html>
<html lang="en">
<head>
<meta charset="utf-8">
<title>Lumen Galley – Business Card</title>
<link rel="stylesheet" href="https://fonts.googleapis.com/css2?family=Inter:wght@400;700&display=swap">
<style>
  :root {
    --backdrop: #232323;
    --card: #171717;
    --card-edge: #1f1f1f;
    --gloss: #5a5a5a;
    --silver: #c9c9c9;
    --white: #f6f6f6;
    --grey: #848484;
  }
  * { margin: 0; padding: 0; box-sizing: border-box; }
  html, body {
    width: 1200px;
    height: 1200px;
    overflow: hidden;
    background: var(--backdrop);
    font-family: "Inter", sans-serif;
  }
  .stage {
    width: 1200px;
    height: 1200px;
    display: flex;
    flex-direction: column;
    align-items: center;
    justify-content: center;
    gap: 60px;
  }
  .card {
    position: relative;
    width: 840px;
    height: 480px;
    background: var(--card);
    border: 1px solid var(--card-edge);
    box-shadow: 0 14px 30px rgba(0, 0, 0, 0.55);
  }
  .card-front {
    display: flex;
    flex-direction: column;
    align-items: center;
    justify-content: center;
    gap: 26px;
  }
  .brand-ring {
    width: 170px;
    height: 170px;
  }
  .brand-name {
    font-size: 30px;
    font-weight: 400;
    letter-spacing: 0.08em;
    text-transform: uppercase;
    color: var(--gloss);
  }
  .card-back {
    display: flex;
    flex-direction: column;
    align-items: center;
    justify-content: center;
    text-align: center;
    padding-bottom: 30px;
  }
  .holder-name {
    font-size: 30px;
    font-weight: 700;
    letter-spacing: 0.62em;
    margin-right: -0.62em;
    text-transform: uppercase;
    color: var(--white);
    margin-bottom: 18px;
  }
  .rule {
    width: 28px;
    height: 1px;
    background: var(--grey);
    margin: 10px 0;
  }
  .contact-line {
    font-size: 20px;
    font-weight: 400;
    letter-spacing: 0.16em;
    color: var(--silver);
    line-height: 1.75;
  }
  .social-handle {
    position: absolute;
    right: 44px;
    bottom: 36px;
    font-size: 14px;
    letter-spacing: 0.08em;
    color: var(--grey);
  }
</style>
</head>
<body>
<main class="stage">
  <section class="card card-front" aria-label="Card front">
    <svg class="brand-ring" viewBox="0 0 170 170" aria-hidden="true">
      <circle cx="85" cy="85" r="80" fill="none" stroke="var(--gloss)" stroke-width="5"/>
    </svg>
    <p class="brand-name">Lumen Galley</p>
  </section>

  <section class="card card-back" aria-label="Card back">
    <h1 class="holder-name">Colin Farrow</h1>
    <div class="rule"></div>
    <p class="contact-line">07812459067</p>
    <p class="contact-line">colinfarrow@lumengalley.com</p>
    <p class="contact-line">www.lumengalley.com</p>
    <div class="rule"></div>
    <p class="contact-line">27 orchard row, Ashvale, bt19 4qd</p>
    <p class="social-handle">lumengalley</p>
  </section>
</main>
</body>
</html>
```